A Clear Three Step Roadmap For Contractors

We are looking for a one-pager "roadmap" that is similar to the 2nd picture we attached, but much more professional & better... please make it landscape orientation. The logo for this system is attached below, as well.

Our Brand Colors to use:
#f2d582
#303030
#8b8c90

The copy we'd like to use on the flyer:
A Clear Three Step Roadmap that will finally allow you to attract quality customers and win more jobs.

The Keystone Ladder Method is a simple to follow system that was created specifically for Contractors and Blue Collar Business Owners.

When it comes to marketing and growing their business, the majority of Contractors are left confused, frustrated and extremely overwhelmed. Unlike most sales, marketing & training programs that offer a single "piece of the puzzle", we've mapped out each essential step of the puzzle and cut out all of the fluff.

All you have to do is complete each step in the right order and we'll be guiding you along the entire journey!

A ---> B

Blueprint: Get clear on where you're going, define your ideal audience, and finally, master your message.
Step 1: Clarify The Chaos
Step 2: Define Your Customer
Step 3: Master Your Message

Build: Attract quality leads, Build your funnel and Formulate a high-converting follow-up system
Step 4: Develop Lead Generator
Step 5: Construct Your Funnel
Step 6: Formulate the Follow-Up

Breakthrough: Get in front of your ideal customers and rapidly scale your business by driving traffic and becoming the authority in your market
Step 7: Turn-On the Traffic
Step 8: Become the Authority
Step 9: Unlock Your Growth

```html
<!DOCTYPE html>
<html lang="en">
<head>
<meta charset="utf-8">
<title>Keystone Ladder Method</title>
<link rel="stylesheet" href="https://fonts.googleapis.com/css2?family=Fredoka:wght@600&family=Open+Sans:wght@400;600&family=Oswald:wght@500;700&display=swap">
<style>
  :root {
    --gold: #f2d582;
    --gold-deep: #d9b650;
    --charcoal: #303030;
    --steel: #8b8c90;
    --wall: #1c1c1c;
    --wall-light: #2a2a2a;
    --white: #ffffff;
    --page: #ffffff;
  }
  * { box-sizing: border-box; margin: 0; padding: 0; }
  html, body {
    width: 818px; height: 1200px; overflow: hidden;
    background: var(--page);
  }
  .roadmap {
    position: absolute; left: 20px; top: 325px;
    width: 778px; height: 550px;
    background: radial-gradient(ellipse at 55% 45%, var(--wall-light), var(--wall) 75%);
    box-shadow: 0 14px 24px rgba(0,0,0,.35);
    overflow: hidden;
  }
  .brand {
    position: absolute; left: 28px; top: 27px;
    display: flex; align-items: center; gap: 8px;
  }
  .brand-mark { width: 30px; height: 30px; background: var(--gold); flex: none; }
  .brand-name {
    font-family: "Open Sans", sans-serif; font-weight: 600;
    color: var(--white); font-size: 15px; line-height: 17px; letter-spacing: .4px;
    text-transform: uppercase;
  }
  .phase-panel {
    position: absolute; left: 28px; top: 82px; width: 186px; height: 374px;
    background: linear-gradient(180deg, #2c2c2c 0%, #555 50%, #2c2c2c 100%);
    border: 3px solid #9a9a9a; border-radius: 4px;
    box-shadow: inset 0 0 0 2px #1a1a1a;
  }
  .phase {
    position: absolute; left: 10px; right: 10px; text-align: center;
    color: var(--white); font-family: "Open Sans", sans-serif;
    font-size: 11px; line-height: 15px;
  }
  .phase-title {
    font-family: "Fredoka", sans-serif; font-weight: 600;
    color: var(--gold); font-size: 15.5px; line-height: 18px; margin-bottom: 2px;
    display: flex; align-items: center; justify-content: center; gap: 5px;
  }
  .phase-num {
    display: inline-flex; align-items: center; justify-content: center;
    width: 13px; height: 13px; border-radius: 2px;
    background: var(--gold); color: var(--charcoal); font-size: 10px; line-height: 1;
  }
  .phase-breakthrough { top: 26px; }
  .phase-build { top: 158px; }
  .phase-blueprint { top: 266px; left: 14px; right: 14px; }
  .divider {
    position: absolute; left: 73px; width: 34px; height: 1px; background: var(--gold-deep);
  }
  .divider-one { top: 139px; }
  .divider-two { top: 246px; }
  .journey-note {
    position: absolute; left: 66px; top: 472px; width: 106px;
    text-align: center; color: var(--white);
    font-family: "Open Sans", sans-serif; font-size: 8.6px; line-height: 12.5px;
  }
  .route { position: absolute; inset: 0; }
  .step-label {
    font-family: "Oswald", sans-serif; font-weight: 500; font-size: 10px;
    fill: var(--white); text-anchor: middle; letter-spacing: .2px;
  }
  .step-num {
    font-family: "Oswald", sans-serif; font-weight: 700; font-size: 20px;
    fill: var(--charcoal); text-anchor: middle;
  }
  .endpoint {
    font-family: "Fredoka", sans-serif; font-weight: 600; font-size: 54px; fill: var(--gold);
  }
  .banner-text {
    font-family: "Fredoka", sans-serif; font-weight: 600; font-size: 18px;
    fill: var(--charcoal); letter-spacing: .6px;
  }
  .icon { fill: none; stroke: var(--charcoal); stroke-width: 1.8; stroke-linejoin: round; stroke-linecap: round; }
  .icon .gold { fill: var(--gold); }
  .icon .steel { fill: var(--steel); }
  .icon .paper { fill: var(--white); }
  .icon .ink { fill: var(--charcoal); stroke: none; }
</style>
</head>
<body>
<main class="roadmap">
  <div class="brand">
    <span class="brand-mark"></span>
    <span class="brand-name">Keystone Ladder<br>Method</span>
  </div>

  <section class="phase-panel">
    <div class="phase phase-breakthrough">
      <h2 class="phase-title"><span class="phase-num">3</span>BREAKTHROUGH</h2>
      <p>Get in front of your ideal customers and rapidly scale your business by driving traffic and becoming the authority in your market</p>
    </div>
    <span class="divider divider-one"></span>
    <div class="phase phase-build">
      <h2 class="phase-title"><span class="phase-num">2</span>BUILD</h2>
      <p>Attract quality leads, Build your funnel and Formulate a high-converting follow-up system</p>
    </div>
    <span class="divider divider-two"></span>
    <div class="phase phase-blueprint">
      <h2 class="phase-title"><span class="phase-num">1</span>BLUEPRINT</h2>
      <p>Get clear on where you're going, define your ideal audience, and finally, master your message.</p>
    </div>
  </section>

  <p class="journey-note">All you have to do is complete each step in the right order and we'll be guiding you along the entire journey!</p>

  <svg class="route" width="778" height="550" viewBox="0 0 778 550">
    <defs>
      <radialGradient id="stepFace" cx="45%" cy="40%" r="65%">
        <stop offset="0" stop-color="#ffffff"/>
        <stop offset="1" stop-color="#e4e4e4"/>
      </radialGradient>
    </defs>

    <g class="path-lines" fill="none" stroke="#f2d582" stroke-width="3">
      <polyline points="237,498 245,498 245,441 329,441"/>
      <line x1="329" y1="441" x2="635" y2="441"/>
      <polyline points="635,441 703,441 703,279 635,279"/>
      <line x1="635" y1="279" x2="329" y2="279"/>
      <polyline points="329,279 245,279 245,117 329,117"/>
      <line x1="329" y1="117" x2="635" y2="117"/>
      <polyline points="635,117 703,117 703,52 710,52"/>
    </g>
    <polygon points="710,46 718,52 710,58" fill="#f2d582"/>

    <text class="endpoint" x="196" y="522">A</text>
    <text class="endpoint" x="716" y="84">B</text>

    <g class="pills" fill="#5c5c5c">
      <rect x="267" y="30" width="124" height="23" rx="6"/>
      <rect x="420" y="30" width="124" height="23" rx="6"/>
      <rect x="573" y="30" width="124" height="23" rx="6"/>
      <rect x="267" y="195" width="124" height="23" rx="6"/>
      <rect x="420" y="195" width="124" height="23" rx="6"/>
      <rect x="573" y="195" width="124" height="23" rx="6"/>
      <rect x="267" y="357" width="124" height="23" rx="6"/>
      <rect x="420" y="357" width="124" height="23" rx="6"/>
      <rect x="573" y="357" width="124" height="23" rx="6"/>
    </g>
    <text class="step-label" x="329" y="46">TURN-ON THE TRAFFIC</text>
    <text class="step-label" x="482" y="46">BECOME THE AUTHORITY</text>
    <text class="step-label" x="635" y="46">UNLOCK YOUR GROWTH</text>
    <text class="step-label" x="329" y="211">FORMULATE THE FOLLOW-UP</text>
    <text class="step-label" x="482" y="211">CONSTRUCT YOUR FUNNEL</text>
    <text class="step-label" x="635" y="211">DEVELOP LEAD GENERATOR</text>
    <text class="step-label" x="329" y="373">CLARIFY THE CHAOS</text>
    <text class="step-label" x="482" y="373">DEFINE YOUR CUSTOMER</text>
    <text class="step-label" x="635" y="373">MASTER YOUR MESSAGE</text>

    <!-- step 7: traffic -->
    <g class="node">
      <rect x="261" y="97" width="32" height="40" rx="3" fill="#f2d582"/>
      <circle cx="329" cy="117" r="50" fill="#f2d582"/>
      <circle cx="329" cy="117" r="43" fill="url(#stepFace)"/>
      <g class="icon" transform="translate(332,117)">
        <rect class="paper" x="-20" y="-16" width="36" height="30" rx="2"/>
        <line x1="-20" y1="-10" x2="16" y2="-10"/>
        <rect class="gold" x="-16" y="-6" width="12" height="9"/>
        <line x1="-16" y1="7" x2="-4" y2="7"/>
        <line x1="-16" y1="10" x2="-8" y2="10"/>
        <circle class="gold" cx="6" cy="-1" r="6"/>
        <circle cx="6" cy="-1" r="2.5"/>
        <line x1="1" y1="8" x2="11" y2="8"/>
        <path class="steel" d="M10 7 L20 14 L15 15 L18 21 L15 22 L12 16 L9 19 Z"/>
      </g>
      <text class="step-num" x="277" y="124">7</text>
    </g>

    <!-- step 8: authority -->
    <g class="node">
      <rect x="414" y="97" width="32" height="40" rx="3" fill="#f2d582"/>
      <circle cx="482" cy="117" r="50" fill="#f2d582"/>
      <circle cx="482" cy="117" r="43" fill="url(#stepFace)"/>
      <g class="icon" transform="translate(485,117)">
        <path class="steel" d="M-24 16 L-2 -10 L8 2 L13 -4 L24 16 Z"/>
        <path class="paper" d="M-9 -2 L-2 -10 L4 -3 L0 -1 L-4 -4 Z"/>
        <line x1="-2" y1="-10" x2="-2" y2="-22"/>
        <path class="gold" d="M-2 -22 L7 -19 L-2 -16 Z"/>
      </g>
      <text class="step-num" x="430" y="124">8</text>
    </g>

    <!-- step 9: growth -->
    <g class="node">
      <rect x="567" y="97" width="32" height="40" rx="3" fill="#f2d582"/>
      <circle cx="635" cy="117" r="50" fill="#f2d582"/>
      <circle cx="635" cy="117" r="43" fill="url(#stepFace)"/>
      <g class="icon" transform="translate(638,117)">
        <path class="gold" d="M-22 20 Q-16 10 -10 16 Q-4 8 0 14 Q4 8 10 16 Q16 10 22 20 Z" stroke="none"/>
        <path class="steel" d="M-7 4 L-12 12 L-7 10 Z M7 4 L12 12 L7 10 Z"/>
        <path class="paper" d="M0 -22 Q8 -12 7 8 L-7 8 Q-8 -12 0 -22 Z"/>
        <path class="ink" d="M0 -22 Q4 -17 5.5 -13 L-5.5 -13 Q-4 -17 0 -22 Z"/>
        <circle class="gold" cx="0" cy="-4" r="3"/>
        <line x1="-3" y1="11" x2="-3" y2="15"/>
        <line x1="3" y1="11" x2="3" y2="15"/>
      </g>
      <text class="step-num" x="583" y="124">9</text>
    </g>

    <!-- step 6: follow-up -->
    <g class="node">
      <rect x="261" y="259" width="32" height="40" rx="3" fill="#f2d582"/>
      <circle cx="329" cy="279" r="50" fill="#f2d582"/>
      <circle cx="329" cy="279" r="43" fill="url(#stepFace)"/>
      <g class="icon" transform="translate(332,279)">
        <rect class="paper" x="-22" y="-17" width="44" height="9" rx="4.5"/>
        <rect class="paper" x="-22" y="-4" width="44" height="9" rx="4.5"/>
        <rect class="paper" x="-22" y="9" width="44" height="9" rx="4.5"/>
        <circle cx="-17" cy="-12.5" r="1.5"/><circle cx="-17" cy="0.5" r="1.5"/><circle cx="-17" cy="13.5" r="1.5"/>
        <line x1="-12" y1="-12.5" x2="-4" y2="-12.5"/>
        <line x1="-12" y1="13.5" x2="-4" y2="13.5"/>
        <circle cx="10" cy="-12.5" r="1"/><circle cx="14" cy="-12.5" r="1"/><circle cx="18" cy="-12.5" r="1"/>
        <circle cx="10" cy="13.5" r="1"/><circle cx="14" cy="13.5" r="1"/><circle cx="18" cy="13.5" r="1"/>
        <path class="gold" d="M0 -10 L9 0 L4 0 L4 12 L-4 12 L-4 0 L-9 0 Z"/>
      </g>
      <text class="step-num" x="277" y="286">6</text>
    </g>

    <!-- step 5: funnel -->
    <g class="node">
      <rect x="414" y="259" width="32" height="40" rx="3" fill="#f2d582"/>
      <circle cx="482" cy="279" r="50" fill="#f2d582"/>
      <circle cx="482" cy="279" r="43" fill="url(#stepFace)"/>
      <g class="icon" transform="translate(485,279)">
        <circle class="ink" cx="-8" cy="-20" r="2"/><circle class="ink" cx="0" cy="-22" r="2.5"/>
        <circle class="ink" cx="8" cy="-18" r="2"/><circle class="ink" cx="-2" cy="-15" r="1.5"/>
        <circle class="ink" cx="12" cy="-23" r="1.5"/>
        <path class="gold" d="M-20 -9 L20 -9 L5 6 L5 21 L-5 17 L-5 6 Z"/>
        <line x1="-17" y1="-5" x2="17" y2="-5"/>
      </g>
      <text class="step-num" x="430" y="286">5</text>
    </g>

    <!-- step 4: lead generator -->
    <g class="node">
      <rect x="567" y="259" width="32" height="40" rx="3" fill="#f2d582"/>
      <circle cx="635" cy="279" r="50" fill="#f2d582"/>
      <circle cx="635" cy="279" r="43" fill="url(#stepFace)"/>
      <g class="icon" transform="translate(638,279) rotate(-40)">
        <path class="gold" d="M-14 -14 L-14 4 A14 14 0 0 0 14 4 L14 -14 L6 -14 L6 4 A6 6 0 0 1 -6 4 L-6 -14 Z"/>
        <rect class="steel" x="-14" y="-20" width="8" height="6"/>
        <rect class="steel" x="6" y="-20" width="8" height="6"/>
        <line x1="-12" y1="-24" x2="-12" y2="-30"/><line x1="-8" y1="-24" x2="-8" y2="-29"/>
        <line x1="8" y1="-24" x2="8" y2="-29"/><line x1="12" y1="-24" x2="12" y2="-30"/>
      </g>
      <text class="step-num" x="583" y="286">4</text>
    </g>

    <!-- step 1: clarify -->
    <g class="node">
      <rect x="261" y="421" width="32" height="40" rx="3" fill="#f2d582"/>
      <circle cx="329" cy="441" r="50" fill="#f2d582"/>
      <circle cx="329" cy="441" r="43" fill="url(#stepFace)"/>
      <g class="icon" transform="translate(332,441)">
        <circle r="19"/>
        <circle r="11"/>
        <line x1="0" y1="-25" x2="0" y2="-9"/>
        <line x1="0" y1="9" x2="0" y2="25"/>
        <line x1="-25" y1="0" x2="-9" y2="0"/>
        <line x1="9" y1="0" x2="25" y2="0"/>
        <circle r="3" fill="#d9b650" stroke="none"/>
      </g>
      <text class="step-num" x="277" y="448">1</text>
    </g>

    <!-- step 2: customer -->
    <g class="node">
      <rect x="414" y="421" width="32" height="40" rx="3" fill="#f2d582"/>
      <circle cx="482" cy="441" r="50" fill="#f2d582"/>
      <circle cx="482" cy="441" r="43" fill="url(#stepFace)"/>
      <g class="icon" transform="translate(485,441)">
        <circle class="gold" cx="0" cy="-11" r="9" stroke="none"/>
        <path class="gold" d="M-20 20 Q-20 2 -7 1 L7 1 Q20 2 20 20 Z" stroke="none"/>
        <path class="paper" d="M-6 1 L0 8 L6 1 Z" stroke="none"/>
        <path class="ink" d="M0 5 L3 9 L0 19 L-3 9 Z"/>
      </g>
      <text class="step-num" x="430" y="448">2</text>
    </g>

    <!-- step 3: message -->
    <g class="node">
      <rect x="567" y="421" width="32" height="40" rx="3" fill="#f2d582"/>
      <circle cx="635" cy="441" r="50" fill="#f2d582"/>
      <circle cx="635" cy="441" r="43" fill="url(#stepFace)"/>
      <g class="icon" transform="translate(638,441)">
        <path class="gold" d="M-18 -6 L-6 -6 L12 -18 L12 14 L-6 2 L-18 2 Z"/>
        <rect class="ink" x="14" y="-20" width="5" height="36" rx="1"/>
        <path class="ink" d="M-12 2 L-5 2 L-3 18 L-9 18 Z"/>
      </g>
      <text class="step-num" x="583" y="448">3</text>
    </g>

    <rect x="264" y="509" width="441" height="28" rx="4" fill="#f2d582"/>
    <g class="pin" fill="none" stroke="#303030" stroke-width="1.8">
      <path d="M322 516 a5.5 5.5 0 0 1 5.5 5.5 c0 4 -5.5 9 -5.5 9 s-5.5 -5 -5.5 -9 a5.5 5.5 0 0 1 5.5 -5.5z"/>
      <circle cx="322" cy="521.5" r="1.8"/>
      <path d="M315 530 h14"/>
    </g>
    <text class="banner-text" x="336" y="530">KEYSTONE LADDER METHOD</text>
  </svg>
</main>
</body>
</html>
```